Banner Ad Designs for tick and flea products

We sell tick and flea products online and want some great banner designs for our online website to promote our tick and flea products.

The ads must be made up in both Flash and HTML5
Ads can be formatted as .JPEG or .GIF files.

Please see the following url for creative requirements
http://help.bannerloop.com/creative-requirements/

Creative licence no limits to your imagination!

Ads must be created in the following sizes:

- Banner – 468×60
- Square – 250×250
- Small Square – 200×200
- Leaderboard – 728×90
- Medium Rectangle – 300×250
- Facebook – 100×72

please view our website at www.globalcritterstore.com.au or .com to get a feel for our website.

The aim is to attract customers who want to save on tick and flea purchases for their pets (dogs and cats)

Target Market(s)

Anyone who owns a dog or cat

Industry/Entity Type

Online

Font styles to use
Sans Serif
Other font styles liked:
• creative licence on font styles

Requirements
Must have
• Must have a strong urge to entice customers to click through.

Images wording and text etc use creative lic
Nice to have
• Strong appeal to dog and cat owners and how they can save on flea and tick essentials.
Keep it simple but effective.
Be fun and playful and inviting.
Should not have
• Please do not use words like cheap - cheapest

Strobing & Flashing - Strobing, flashing backgrounds, or otherwise distracting ads are not allowed. Do not attempt to overtly distract the user from page content.

```html
<!DOCTYPE html>
<html lang="en">
<head>
<meta charset="utf-8">
<title>Banner – 468×60 concepts</title>
<link rel="stylesheet" href="https://fonts.googleapis.com/css2?family=PT+Sans:wght@400;700&family=Arimo:wght@700&display=swap">
<style>
  :root {
    --stage: #6b6b6b;
    --page: #ffffff;
    --ink: #111111;
    --leaf: #7ba82d;
    --leaf-dark: #5f8a1c;
    --cream: #f4f1ea;
    --tan: #c9a677;
    --fur: #6b4a2e;
    --button-top: #5fd06a;
    --button-bottom: #1f9a33;
    --button-ink: #174a1f;
    --burst: #d9ecf7;
    --burst-edge: #8fb6d1;
    --burst-ink: #2d5f9a;
    --white: #ffffff;
  }
  * { box-sizing: border-box; margin: 0; padding: 0; }
  html, body {
    width: 1200px; height: 900px; overflow: hidden;
    background: var(--page);
    font-family: "PT Sans", sans-serif;
  }
  .stage {
    position: absolute; left: 0; top: 0;
    width: 1200px; height: 579px;
    background: var(--stage);
  }
  .variant-label {
    position: absolute; left: 190px; width: 42px;
    font-size: 54px; line-height: 90px; text-align: center;
    color: var(--ink);
  }
  .banner {
    position: absolute; left: 277px;
    width: 702px; height: 90px;
    background: var(--leaf);
    overflow: hidden;
  }
  .banner--a { top: 83px; }
  .banner--b { top: 190px; }
  .banner--c { top: 301px; }
  .banner--d { top: 415px; }
  .photo-pets {
    position: absolute; left: 0; top: 0;
    width: 140px; height: 90px;
    background: linear-gradient(90deg, var(--cream) 0%, #d8c6ad 35%, #a88a66 60%, var(--leaf) 100%);
  }
  .photo-pugs {
    position: absolute; right: 0; top: 0;
    width: 128px; height: 90px;
    background: linear-gradient(90deg, var(--leaf) 0%, var(--tan) 30%, #dcc39a 60%, var(--fur) 100%);
  }
  .headline {
    position: absolute; top: 0; height: 90px;
    display: flex; align-items: center; justify-content: center;
    color: var(--white); text-align: center;
    font-weight: 700;
  }
  .banner--a .headline { left: 140px; right: 128px; font-size: 32px; line-height: 36px; }
  .banner--b .headline { left: 140px; right: 128px; font-size: 38px; }
  .banner--c .headline { left: 140px; right: 190px; font-size: 37px; }
  .brand-panel {
    position: absolute; right: 0; top: 0;
    width: 192px; height: 90px;
    background: var(--white);
    border-radius: 45px 0 0 45px;
    display: flex; align-items: center; gap: 8px;
    padding-left: 14px;
  }
  .brand-dot {
    width: 16px; height: 16px; border-radius: 50%;
    background: var(--leaf); flex: none;
  }
  .brand-name {
    font-size: 21px; line-height: 22px; font-weight: 700;
    color: var(--leaf-dark);
  }
  .free-shipping {
    position: absolute; left: 12px; top: 3px;
    width: 86px; height: 84px;
  }
  .order-button {
    position: absolute; left: 213px; top: 20px;
    width: 195px; height: 52px;
    border-radius: 6px;
    border: 2px solid #2e7a2c;
    background: linear-gradient(180deg, var(--button-top) 0%, #3cb84a 50%, var(--button-bottom) 100%);
    color: var(--button-ink);
    font-family: "Arimo", sans-serif; font-weight: 700;
    font-size: 27px; letter-spacing: 0.5px;
    display: flex; align-items: center; justify-content: center;
    text-decoration: none;
  }
  .size-caption {
    position: absolute; top: 610px; left: 0; width: 1200px;
    text-align: center; font-size: 34px; color: var(--ink);
  }
</style>
</head>
<body>
  <main class="stage">
    <div class="variant-label" style="top:83px">A</div>
    <div class="banner banner--a">
      <div class="photo-pets" role="img" aria-label="Photo of a small dog and a tabby cat"></div>
      <p class="headline">Save on genuine brand<br>tick and flea products</p>
      <div class="photo-pugs" role="img" aria-label="Photo of three pugs in a row"></div>
    </div>

    <div class="variant-label" style="top:190px">B</div>
    <div class="banner banner--b">
      <div class="photo-pets" role="img" aria-label="Photo of a small dog and a tabby cat"></div>
      <p class="headline">Protect Your Pets!</p>
      <div class="photo-pugs" role="img" aria-label="Photo of three pugs in a row"></div>
    </div>

    <div class="variant-label" style="top:301px">C</div>
    <div class="banner banner--c">
      <div class="photo-pets" role="img" aria-label="Photo of a small dog and a tabby cat"></div>
      <p class="headline">Save with us</p>
      <div class="brand-panel"><span class="brand-dot"></span><span class="brand-name">Global Critter<br>Store</span></div>
    </div>

    <div class="variant-label" style="top:415px">D</div>
    <div class="banner banner--d">
      <svg class="free-shipping" viewBox="0 0 86 84" aria-label="Free Shipping">
        <polygon fill="var(--burst)" stroke="var(--burst-edge)" stroke-width="1.5"
          points="43,2 50,14 63,6 64,21 79,19 73,33 85,42 73,51 79,65 64,63 63,78 50,70 43,82 36,70 23,78 22,63 7,65 13,51 1,42 13,33 7,19 22,21 23,6 36,14"/>
        <text x="43" y="38" text-anchor="middle" font-family="Arimo, sans-serif" font-weight="700" font-size="15" fill="var(--burst-ink)" transform="rotate(-12 43 42)">Free</text>
        <text x="43" y="54" text-anchor="middle" font-family="Arimo, sans-serif" font-weight="700" font-size="12" fill="var(--burst-ink)" transform="rotate(-12 43 42)">Shipping</text>
      </svg>
      <a class="order-button" href="#">ORDER NOW</a>
      <div class="brand-panel"><span class="brand-dot"></span><span class="brand-name">Global Critter<br>Store</span></div>
    </div>
  </main>
  <p class="size-caption">Banner – 468×60</p>
</body>
</html>
```